QM active wear

Hey There

QM is a brand new active wear Sydney base company. our clothe design by professional dancers & athletics. pushing the niche market of active wear. the products we have is cool fashionable functional Eco friendly!!!

it caters male and female. who stays active and wants to be chic at the same time.
we would like to be associate with K-8 & Coastal garments & Vorn kind of brands.

i need you guys to use the existing logo to restructure it. turn it into consistent format that can be shared through out all the electronic business stationery. pls refer to all the photos i have upload in this brief. hopefully it'll gives you guys more of what i like i needs to be done.

PS: business card material specifications needs to be provided.
just so send the details to the printing company without explain too much.

Cheers

Industry/Entity Type

Electronic

Requirements
Must have
• It needs be more readable. clean. current. pop. fashionable.
interesting details across the broad for all electronic stationary.

for you to think about it and working on : company's business letters, order forms, its notices and other official publications, promissory notes, endorsements, cheques and orders for money or goods purporting to be signed by, or on behalf of, the company invoices, receipts websites

```html
<!DOCTYPE html>
<html lang="en">
<head>
<meta charset="utf-8">
<title>QM Active Wear – Stationery</title>
<link href="https://fonts.googleapis.com/css2?family=Montserrat:wght@400;500;600&display=swap" rel="stylesheet">
<style>
:root{
  --backdrop:#868786;
  --paper:#ffffff;
  --ink:#333333;
  --band:#353535;
  --black:#0e0f0f;
  --teal:#1ca89e;
  --mark-grey:#3a3a3a;
  --light:#ffffff;
}
*{margin:0;padding:0;box-sizing:border-box}
html,body{width:1200px;height:1000px;overflow:hidden}
body{background:var(--backdrop);font-family:"Montserrat",sans-serif;color:var(--ink);position:relative}
.sheet,.card,.envelope{position:absolute}
.abs{position:absolute}

/* brand lockup: one plain circle + name in one colour/weight */
.lockup{position:absolute;display:flex;align-items:center;gap:8px}
.lockup .dot{border-radius:50%;flex:none}
.lockup .name{font-weight:600;line-height:.95;text-transform:uppercase;letter-spacing:.5px;white-space:nowrap}

/* letterhead */
.letterhead{left:45px;top:45px;width:573px;height:742px;background:var(--paper)}
.letterhead .top-band{left:0;top:15px;width:410px;height:24px;background:var(--band);border-radius:0 12px 12px 0}
.contact-row{left:33px;top:44px;display:flex;gap:14px;font-size:8.5px;font-weight:500}
.contact-row span,.contact-list div{display:flex;align-items:center;gap:4px}
.letterhead .footer-address{left:0;right:0;top:713px;text-align:center;font-size:8.5px;font-weight:500}
.letterhead .bottom-band{left:0;bottom:0;width:100%;height:10px;background:var(--band)}

/* envelope */
.envelope{left:92px;top:350px;width:600px;height:300px;background:var(--paper);box-shadow:0 2px 6px rgba(0,0,0,.35)}
.envelope .top-band{left:0;top:42px;width:70px;height:26px;background:var(--band)}
.envelope .contact-list{left:70px;top:112px;font-size:9px;line-height:14px;font-weight:500}
.envelope .bottom-band{left:0;bottom:0;width:100%;height:48px;background:var(--band)}

/* business cards */
.card{width:267px;height:165px;left:872px;overflow:hidden}
.card.dark{background:var(--black)}
.person .name{font-size:10px;font-weight:500;text-transform:uppercase}
.person .role{font-size:6.5px;margin-top:2px}
.contact-list.small{font-size:6.5px;line-height:10px;font-weight:500}
.on-dark{color:var(--light)}
.teal{color:var(--teal)}
.split-left{left:0;top:0;width:140px;height:165px;background:var(--black)}
.white-base{background:var(--paper)}
.top-black{left:0;top:0;width:100%;height:88px;background:var(--black)}
.divider{width:1px;background:var(--teal);height:42px}
.stacked{flex-direction:column;align-items:flex-start;gap:9px}
.back-teal{left:580px;top:793px;width:266px;height:165px;background:var(--teal);position:absolute}
.big-circle{border-radius:50%;background:var(--mark-grey);position:absolute}
</style>
</head>
<body>

<!-- Letterhead -->
<section class="sheet letterhead" aria-label="Letterhead">
  <div class="abs top-band"></div>
  <div class="lockup" style="left:402px;top:16px">
    <span class="dot" style="width:52px;height:52px;background:var(--mark-grey)"></span>
    <span class="name" style="font-size:17px;color:var(--ink)">QM<br>Active<br>Wear</span>
  </div>
  <div class="abs contact-row">
    <span><svg width="6" height="9" viewBox="0 0 6 9"><rect x=".5" y=".5" width="5" height="8" rx="1" fill="none" stroke="#1ca89e"/></svg>+86 400118273</span>
    <span><svg width="7" height="6" viewBox="0 0 7 6"><rect width="7" height="6" fill="#1ca89e"/></svg>qmactivewear@mail.com</span>
  </div>
  <p class="abs footer-address">Po Box 418, Harbour Hills, Sydney, NSW Australia 2031</p>
  <div class="abs bottom-band"></div>
</section>

<!-- Envelope -->
<section class="envelope" aria-label="Envelope">
  <div class="abs top-band"></div>
  <div class="lockup" style="left:68px;top:38px">
    <span class="dot" style="width:48px;height:48px;background:var(--mark-grey)"></span>
    <span class="name" style="font-size:17px;color:var(--ink)">QM<br>Active<br>Wear</span>
  </div>
  <div class="abs contact-list">
    <div>+86 400118273</div>
    <div>qmactivewear@mail.com</div>
    <div>Po Box 418, Harbour Hills,</div>
    <div>Sydney, NSW Australia 2031</div>
  </div>
  <div class="abs bottom-band"></div>
</section>

<!-- Card 1: all dark -->
<section class="card dark" style="top:42px" aria-label="Business card front, dark">
  <div class="lockup stacked" style="left:26px;top:20px">
    <span class="dot" style="width:44px;height:44px;background:var(--teal)"></span>
    <span class="name" style="font-size:22px;color:var(--light)">QM<br>Active<br>Wear</span>
  </div>
  <div class="abs person on-dark" style="left:155px;top:22px"><div class="name">Marcus Hale</div><div class="role">Founder</div></div>
  <div class="abs contact-list small on-dark" style="left:155px;top:98px">
    <div>+86 400118273</div><div>qmactivewear@mail.com</div>
    <div>Po Box 418 Harbour Hills</div><div>Sydney, NSW Australia 2031</div>
  </div>
</section>

<!-- Card 2: split -->
<section class="card white-base" style="top:232px" aria-label="Business card front, split">
  <div class="abs split-left"></div>
  <div class="lockup stacked" style="left:26px;top:20px">
    <span class="dot" style="width:44px;height:44px;background:var(--teal)"></span>
    <span class="name" style="font-size:22px;color:var(--light)">QM<br>Active<br>Wear</span>
  </div>
  <div class="abs person" style="left:155px;top:20px"><div class="name teal">Marcus Hale</div><div class="role">Founder</div></div>
  <div class="abs contact-list small" style="left:155px;top:101px">
    <div>+86 400118273</div><div>qmactivewear@mail.com</div>
    <div>Po Box 418 Harbour Hills</div><div>Sydney, NSW Australia 2031</div>
  </div>
</section>

<!-- Card 3: black top, white base -->
<section class="card white-base" style="top:424px" aria-label="Business card front, banded">
  <div class="abs top-black"></div>
  <div class="lockup" style="left:66px;top:20px">
    <span class="dot" style="width:42px;height:42px;background:var(--teal)"></span>
    <span class="name" style="font-size:21px;color:#7a7a7a">QM Active<br>Wear</span>
  </div>
  <div class="abs person" style="left:27px;top:108px"><div class="name teal">Marcus Hale</div><div class="role">Founder</div></div>
  <div class="abs divider" style="left:145px;top:100px"></div>
  <div class="abs contact-list small" style="left:153px;top:100px">
    <div>+86 400118273</div><div>qmactivewear@mail.com</div>
    <div>Po Box 418 Harbour Hills</div><div>Sydney, NSW Australia 2031</div>
  </div>
</section>

<!-- Card 4 -->
<section class="card white-base" style="top:615px" aria-label="Business card front, banded white logo">
  <div class="abs top-black"></div>
  <div class="lockup" style="left:56px;top:20px">
    <span class="dot" style="width:46px;height:46px;background:var(--teal)"></span>
    <span class="name" style="font-size:22px;color:var(--light)">QM Active<br>Wear</span>
  </div>
  <div class="abs person" style="left:27px;top:107px"><div class="name teal">Marcus Hale</div><div class="role">Founder</div></div>
  <div class="abs divider" style="left:145px;top:100px"></div>
  <div class="abs contact-list small" style="left:153px;top:100px">
    <div>+86 400118273</div><div>qmactivewear@mail.com</div>
    <div>Po Box 418 Harbour Hills</div><div>Sydney, NSW Australia 2031</div>
  </div>
</section>

<!-- Card backs -->
<section class="back-teal" aria-label="Business card back, teal">
  <span class="big-circle" style="left:81px;top:30px;width:104px;height:104px"></span>
</section>
<section class="card dark" style="top:793px" aria-label="Business card back, black">
  <span class="big-circle" style="left:81px;top:30px;width:104px;height:104px"></span>
</section>

</body>
</html>
```